Venmar Tolu Holdings Limited is a asset management company and project funding company, we specialise in high end finance for high net worth individuals, we are looking for a new logo letterhead template, email footer template and business card design. The letterhead template should be designed in word format so that the letterheading can be used electronically.

Below is the current logo that is a but plain and a little cheaper looking, colour schemes are not important just that it looks professional.

I am looking for a sharp impact that stands out,

Target Market(s)

High net worth individuals and institutions

Industry/Entity Type

Finance

Contact Information for Business Card

Venmar Tolu Holdings Limited
T: 0333 418 2960

M: 07631 942017
E:derek.hollin@venmar-toluholdings.example

CORAL MEADE, EAST HARBOUR ROAD
SECOND FLOOR, SUITE 410
P.O. BOX DK-48731
NASSAU BAHAMAS

Logo Text

Font styles to use
Serif
Sans Serif
Script
Other font styles liked:
• Tahoma

Colors
fbed22
6b449b
ec1f27
f78f20
33b8a4
0592cd

Requirements
Must have
• Colours schemes would look good in blue’s green’s purples.

Yellow and Purple together maybe a nice combination.
Nice to have
• I want the log to look sharpe, relate to a global presence, but I also want to it to look established.
Should not have
• N/a

```html
<!DOCTYPE html>
<html lang="en">
<head>
<meta charset="utf-8">
<title>Venmar Tolu Holdings Limited – Stationery</title>
<link rel="stylesheet" href="https://fonts.googleapis.com/css2?family=Montserrat:wght@400;500;700;800&display=swap">
<style>
  :root{
    --green:#63bf45;
    --green-dark:#3f9a37;
    --purple:#6b449b;
    --purple-light:#8a6bb8;
    --ink:#2b2b2e;
    --band:#3a3a3d;
    --card:#141414;
    --paper:#ffffff;
    --stage:#ececec;
    --stage-light:#f6f6f6;
    --navy-top:#25364a;
    --navy-bottom:#101a26;
    --muted:#8a8a8f;
    --white:#ffffff;
  }
  *{box-sizing:border-box;margin:0;padding:0}
  html,body{width:1200px;height:2508px;overflow:hidden}
  body{font-family:"Montserrat",sans-serif;color:var(--ink);background:var(--stage)}

  .section{position:absolute;left:0;width:1200px}
  .letterhead-stage{top:0;height:832px;background:var(--stage)}
  .cards-stage{top:832px;height:728px;background:var(--stage-light)}
  .contact-band{top:1560px;height:460px;background:var(--band)}
  .brand-stage{top:2020px;height:488px;background:radial-gradient(ellipse at 50% 40%,var(--navy-top),var(--navy-bottom) 75%)}

  /* brand lockup */
  .lockup{display:flex;align-items:center;gap:16px}
  .lockup-dot{border-radius:50%;background:var(--purple);flex:none}
  .lockup-name{font-weight:800;text-transform:uppercase;line-height:1.05;letter-spacing:.02em}

  /* letterhead */
  .letterhead{position:absolute;left:322px;top:40px;width:556px;height:760px;background:var(--paper);box-shadow:0 6px 22px rgba(0,0,0,.18);overflow:hidden}
  .letterhead .lockup{position:absolute;left:212px;top:40px;gap:8px}
  .letterhead .lockup-dot{width:26px;height:26px}
  .letterhead .lockup-name{font-size:11px;color:var(--green-dark)}
  .letterhead-contact{position:absolute;right:30px;top:38px;list-style:none;font-size:6.5px;color:var(--muted);line-height:12px}
  .letterhead-contact li{display:flex;align-items:center;gap:5px}
  .letterhead-contact i{display:inline-block;width:7px;height:7px;background:var(--green);border-radius:1px}
  .letterhead-waves{position:absolute;left:0;bottom:0;width:556px;height:90px}

  /* business cards */
  .card{position:absolute;top:232px;width:460px;height:262px;background:var(--card);border-radius:4px;box-shadow:0 10px 26px rgba(0,0,0,.3);overflow:hidden}
  .card-front{left:110px}
  .card-back{left:630px}
  .card-front .lockup{position:absolute;left:50%;top:50%;transform:translate(-50%,-50%)}
  .card-front .lockup-dot{width:50px;height:50px}
  .card-front .lockup-name{font-size:21px;color:var(--green)}
  .card-back .lockup{position:absolute;left:30px;top:28px;gap:10px}
  .card-back .lockup-dot{width:30px;height:30px}
  .card-back .lockup-name{font-size:13px;color:var(--green)}
  .card-back-details{position:absolute;left:30px;top:104px;list-style:none;font-size:10px;color:var(--white);line-height:17px}
  .card-back-details .label{color:var(--green);font-weight:700;display:inline-block;width:16px}
  .card-back-address{position:absolute;right:28px;bottom:28px;text-align:right;font-size:8.5px;color:#bdbdbd;line-height:13px;letter-spacing:.04em}
  .card-back-stripe{position:absolute;left:0;bottom:0;width:100%;height:6px;background:linear-gradient(90deg,var(--green),var(--purple))}

  /* contact band */
  .contact-band .lockup{position:absolute;left:120px;top:150px;gap:20px}
  .contact-band .lockup-dot{width:96px;height:96px}
  .contact-band .lockup-name{font-size:34px;color:var(--green)}
  .band-details{position:absolute;right:110px;top:98px;text-align:right}
  .band-title{font-size:40px;font-weight:800;color:var(--white);line-height:1}
  .band-title small{display:block;font-size:24px;font-weight:700;margin-top:4px}
  .band-list{list-style:none;margin-top:22px}
  .band-list li{display:flex;justify-content:flex-end;align-items:center;gap:14px;font-size:17px;font-weight:500;color:var(--white);letter-spacing:.03em;height:36px}
  .band-icon{width:24px;height:24px;background:var(--white);border-radius:3px;display:flex;align-items:center;justify-content:center}
  .band-icon svg{width:16px;height:16px}

  /* brand display */
  .brand-stage .lockup{position:absolute;left:50%;top:50%;transform:translate(-50%,-50%);flex-direction:column;gap:22px;text-align:center}
  .brand-stage .lockup-dot{width:150px;height:150px}
  .brand-stage .lockup-name{font-size:46px;color:var(--green)}
</style>
</head>
<body>

<section class="section letterhead-stage">
  <article class="letterhead">
    <div class="lockup">
      <span class="lockup-dot"></span>
      <span class="lockup-name">Venmar Tolu<br>Holdings Limited</span>
    </div>
    <ul class="letterhead-contact">
      <li><i></i>0333 418 2960</li>
      <li><i></i>07631 942017</li>
      <li><i></i>derek.hollin@venmar-toluholdings.example</li>
      <li><i></i>www.venmar-toluholdings.example</li>
    </ul>
    <svg class="letterhead-waves" viewBox="0 0 556 90" preserveAspectRatio="none" aria-hidden="true">
      <path d="M0 40 C150 85 330 20 556 30 L556 90 L0 90 Z" fill="var(--green)"/>
      <path d="M0 62 C170 96 360 44 556 54 L556 90 L0 90 Z" fill="var(--purple-light)"/>
      <path d="M0 76 C180 100 380 66 556 72 L556 90 L0 90 Z" fill="var(--purple)"/>
    </svg>
  </article>
</section>

<section class="section cards-stage">
  <article class="card card-front">
    <div class="lockup">
      <span class="lockup-dot"></span>
      <span class="lockup-name">Venmar Tolu<br>Holdings Limited</span>
    </div>
  </article>
  <article class="card card-back">
    <div class="lockup">
      <span class="lockup-dot"></span>
      <span class="lockup-name">Venmar Tolu<br>Holdings Limited</span>
    </div>
    <ul class="card-back-details">
      <li><span class="label">T</span>0333 418 2960</li>
      <li><span class="label">M</span>07631 942017</li>
      <li><span class="label">E</span>derek.hollin@venmar-toluholdings.example</li>
      <li><span class="label">W</span>www.venmar-toluholdings.example</li>
    </ul>
    <address class="card-back-address" style="font-style:normal">
      CORAL MEADE, EAST HARBOUR ROAD<br>
      SECOND FLOOR, SUITE 410<br>
      P.O. BOX DK-48731<br>
      NASSAU BAHAMAS
    </address>
    <span class="card-back-stripe"></span>
  </article>
</section>

<section class="section contact-band">
  <div class="lockup">
    <span class="lockup-dot"></span>
    <span class="lockup-name">Venmar Tolu<br>Holdings Limited</span>
  </div>
  <div class="band-details">
    <h1 class="band-title">VENMAR TOLU<small>HOLDINGS LIMITED</small></h1>
    <ul class="band-list">
      <li>0333 418 2960
        <span class="band-icon"><svg viewBox="0 0 16 16"><path d="M4 2 L6 2 L7 5 L5.5 6.5 C6.5 8.5 7.5 9.5 9.5 10.5 L11 9 L14 10 L14 12 C14 13 13 14 12 14 C6.5 14 2 9.5 2 4 C2 3 3 2 4 2 Z" fill="var(--band)"/></svg></span>
      </li>
      <li>07631 942017
        <span class="band-icon"><svg viewBox="0 0 16 16"><rect x="4.5" y="1.5" width="7" height="13" rx="1.2" fill="none" stroke="var(--band)" stroke-width="1.6"/><circle cx="8" cy="12" r="0.9" fill="var(--band)"/></svg></span>
      </li>
      <li>DEREK.HOLLIN@VENMAR-TOLUHOLDINGS.EXAMPLE
        <span class="band-icon"><svg viewBox="0 0 16 16"><rect x="2" y="4" width="12" height="8.5" fill="none" stroke="var(--band)" stroke-width="1.5"/><path d="M2 4 L8 9 L14 4" fill="none" stroke="var(--band)" stroke-width="1.5"/></svg></span>
      </li>
      <li>WWW.VENMAR-TOLUHOLDINGS.EXAMPLE
        <span class="band-icon"><svg viewBox="0 0 16 16"><circle cx="8" cy="8" r="5.5" fill="none" stroke="var(--band)" stroke-width="1.5"/><path d="M2.5 8 H13.5 M8 2.5 C5.5 5 5.5 11 8 13.5 M8 2.5 C10.5 5 10.5 11 8 13.5" fill="none" stroke="var(--band)" stroke-width="1.2"/></svg></span>
      </li>
    </ul>
  </div>
</section>

<section class="section brand-stage">
  <div class="lockup">
    <span class="lockup-dot"></span>
    <span class="lockup-name">Venmar Tolu<br>Holdings Limited</span>
  </div>
</section>

</body>
</html>
```